Boat and Caravan indoor/ outdoor storage

A new company that provides 4star indoor and outdoor storage for Boats and Caravans
Industry/Entity Type
It Company

```html
<!DOCTYPE html>
<html lang="en">
<head>
<meta charset="UTF-8">
<title>Boat &amp; Caravan Storage Flyer</title>
<link href="https://fonts.googleapis.com/css2?family=Oswald:wght@400;500;600&family=Open+Sans:wght@400;600&display=swap" rel="stylesheet">
<style>
  :root {
    --teal: #1a9ea6;
    --teal-dark: #127b82;
    --ink: #2b2b33;
    --navy: #1f2530;
    --paper: #f4f5f6;
    --white: #ffffff;
  }
  * { margin: 0; padding: 0; box-sizing: border-box; }
  html, body { width: 900px; height: 1200px; overflow: hidden; background: var(--paper); }
  .flyer { position: relative; width: 900px; height: 1200px; background: var(--paper); overflow: hidden; }
  .shapes { position: absolute; inset: 0; }
  .about-title {
    position: absolute; left: 44px; top: 470px;
    font: 500 34px/1 "Oswald", sans-serif; color: var(--teal); letter-spacing: 1px;
  }
  .about-text {
    position: absolute; left: 44px; top: 522px; width: 400px;
    font: 400 16px/1.45 "Open Sans", sans-serif; color: var(--ink); text-align: justify;
  }
  .headline {
    position: absolute; left: 478px; top: 500px; width: 400px;
    font-family: "Oswald", sans-serif; color: var(--navy); text-transform: uppercase;
  }
  .headline span { display: block; white-space: nowrap; }
  .headline .line-main { font-weight: 500; font-size: 60px; line-height: 1.05; }
  .headline .line-sub { font-weight: 500; font-size: 30px; line-height: 1.3; }
  .headline .line-accent { font-weight: 500; font-size: 62px; line-height: 1.05; color: var(--teal); }
  .highlights {
    position: absolute; left: 44px; top: 880px; width: 430px;
    font: 500 26px/1.2 "Oswald", sans-serif; color: var(--navy); text-transform: uppercase;
  }
  .website {
    position: absolute; left: 0; right: 0; top: 1128px; text-align: center;
    font: 500 26px/1 "Oswald", sans-serif; color: var(--white); letter-spacing: 6px;
  }
</style>
</head>
<body>
<main class="flyer">
  <svg class="shapes" viewBox="0 0 900 1200" width="900" height="1200">
    <defs>
      <linearGradient id="heroTones" x1="0" y1="0" x2="0" y2="1">
        <stop offset="0" stop-color="#b9d3e6"/>
        <stop offset="0.45" stop-color="#7fa36b"/>
        <stop offset="1" stop-color="#9a9c98"/>
      </linearGradient>
      <linearGradient id="interiorTones" x1="0" y1="0" x2="1" y2="1">
        <stop offset="0" stop-color="#e8d6b8"/>
        <stop offset="0.5" stop-color="#b07a4a"/>
        <stop offset="1" stop-color="#6e3f24"/>
      </linearGradient>
    </defs>

    <polygon points="0,0 900,0 900,360 390,455 0,395" fill="url(#heroTones)" role="img" aria-label="Photo of a white motorhome caravan parked beside a motor boat on a trailer"/>
    <polygon points="0,395 390,455 900,360 900,380 390,478 0,418" fill="var(--navy)"/>
    <polygon points="0,418 390,478 560,446 390,500 0,436" fill="var(--teal)"/>
    <polygon points="600,438 900,380 900,410 760,438" fill="var(--teal)"/>

    <polygon points="560,720 900,700 900,1040 520,1040 470,880" fill="var(--teal)"/>
    <polygon points="580,740 880,724 880,1010 540,1010 495,880" fill="url(#interiorTones)" role="img" aria-label="Photo of a boat cabin interior with wooden panelling and seating"/>

    <polygon points="0,1060 120,1040 450,1095 780,1040 900,1060 900,1200 0,1200" fill="var(--teal)"/>
    <polygon points="0,1060 120,1040 450,1095 780,1040 900,1060 900,1070 780,1052 450,1108 120,1052 0,1072" fill="var(--teal-dark)"/>
  </svg>

  <h2 class="about-title">ABOUT US</h2>
  <p class="about-text">We are a new storage company offering four star indoor and outdoor storage for boats and caravans. Our secure site is monitored around the clock with CCTV, gated access and regular patrols, so your vessel or van is always in safe hands. Indoor bays keep your boat or caravan dry, clean and protected from frost, sun and storms, while our spacious outdoor pitches give easy drive-in access whenever you need it. Flexible monthly and yearly plans, on-site washing and battery care mean you are ready for the water or the road.</p>

  <h1 class="headline">
    <span class="line-main">Safe Storage</span>
    <span class="line-sub">for your boat and caravan</span>
    <span class="line-accent">4 Star Care</span>
  </h1>

  <p class="highlights">Indoor and outdoor bays for every size of boat and caravan</p>

  <p class="website">WWW.YOURWEBSITE.COM</p>
</main>
</body>
</html>
```